Web Design Project for DJ

We need a web design for a DJ. Our client is a freelance DJ who already has a regular gig at a major night club but is looking to expand his exposure. He is located in a major metropolitan area and is looking for further gigs. He is hoping to generate further business via the website, including bookings via the site.

For reference his pagelinker page is here https://www.pagelinker.example/pages/DJ-Vorn/730162948415207

Following face to face discussions with the client today we have made a few small alterations to the brief.  We are hoping to have some images uploaded shortly.

Target Market(s)

Event planners, night club owners, radio stations, younger age groups (16-35)

Industry/Entity Type

Business

Requirements
Must have
• Name is DJVorn, this should obviously feature prominently. His current business card is attached as an example.

Links to Pagelinker and Tunedrift

Cool, modern look, slightly edgy.

Site will be built in Joomla, so a front page and secondary page template is required.
Nice to have
• Blog style layout to front page featuring recent and upcoming gigs.

Secondary pages may include a more expansive blog, a list of upcoming gigs, and a booking form.

Darker colour palettes preferred and use of same/similar fonts to those on the business card are an obvious plus

```html
<!DOCTYPE html>
<html lang="en">
<head>
<meta charset="utf-8">
<title>DJ-Vorn</title>
<link rel="stylesheet" href="https://fonts.googleapis.com/css2?family=Oswald:wght@300;400;700&family=Arimo:wght@400;700&display=swap">
<style>
  :root {
    --bg-page: #333333;
    --bg-header: #1c1c1c;
    --bg-footer: #050505;
    --text-light: #ffffff;
    --text-muted: #9a9a9a;
    --text-grey: #b0b0b0;
    --accent-blue: #1e8fd0;
    --accent-blue-dark: #0d5f9b;
    --accent-green: #52b83a;
    --divider: #777777;
    --circle: #8a8a8a;
  }
  * { margin: 0; padding: 0; box-sizing: border-box; }
  html, body { width: 1200px; height: 1185px; overflow: hidden; background: var(--bg-page); }
  body { position: relative; font-family: "Arimo", Arial, sans-serif; color: var(--text-light); }
  a { color: inherit; text-decoration: none; }

  /* Header */
  .site-header {
    position: absolute; left: 0; top: 0; width: 1200px; height: 76px;
    background: linear-gradient(#2a2a2a, #161616 60%, #202020);
  }
  .brand { position: absolute; left: 39px; top: 14px; display: flex; align-items: center; gap: 10px;
    font-family: "Oswald", sans-serif; font-weight: 700; font-size: 38px; line-height: 46px; color: var(--text-light); }
  .brand-dot { width: 40px; height: 40px; border-radius: 50%; background: var(--text-light); }
  .main-nav a { position: absolute; top: 16px; font-family: "Oswald", sans-serif; font-weight: 300;
    font-size: 17px; color: #d8d8d8; }

  /* Hero */
  .hero { position: absolute; left: 0; top: 76px; width: 1200px; height: 481px;
    background: radial-gradient(ellipse at 50% 45%, #3a3a3a 0%, #121212 55%, #050505 100%); }
  .hero-dj { position: absolute; left: 367px; top: 0; width: 345px; height: 345px;
    background: linear-gradient(#4a4a55, #2c2c34); border-radius: 40% 40% 0 0; }
  .hero-decks { position: absolute; left: 76px; top: 330px; width: 1040px; height: 135px;
    background: linear-gradient(#2a2a2a, #0d0d0d); border-radius: 20px 20px 60px 60px; }
  .hero-text { position: absolute; font-family: "Oswald", sans-serif; font-weight: 300;
    font-size: 26px; line-height: 32px; text-align: center; color: #e8e8e8; }
  .hero-text .venue { color: var(--accent-blue); font-weight: 700; }
  .hero-text .night { color: var(--accent-green); font-weight: 400; }

  .band { position: absolute; left: 0; top: 557px; width: 1200px; height: 31px;
    background: linear-gradient(#4a4a4a, #3a3a3a 50%, #333); }

  /* Content */
  .booking-btn { position: absolute; left: 27px; top: 595px; width: 310px; height: 64px;
    border-radius: 32px; background: #151515; padding: 6px; }
  .booking-btn span { display: block; height: 100%; border-radius: 26px;
    background: linear-gradient(#3aa6e6, var(--accent-blue) 50%, var(--accent-blue-dark));
    font-family: "Oswald", sans-serif; font-weight: 300; font-size: 30px; line-height: 52px;
    text-align: center; color: var(--text-light); }

  .section-title { position: absolute; font-family: "Oswald", sans-serif; }
  .recent-title { left: 37px; top: 693px; font-weight: 300; font-size: 38px; color: #bdbdbd; }
  .upcoming-title { left: 637px; top: 604px; font-weight: 700; font-size: 34px; color: var(--text-grey); letter-spacing: 0.5px; }

  .gig-thumb { position: absolute; left: 37px; width: 100px; height: 85px;
    background: linear-gradient(135deg, #1b2a4a, #3b4a6a); }
  .gig-thumb.alt { background: linear-gradient(135deg, #2e6a2e, #202020); }
  .gig-date { position: absolute; left: 160px; font-family: "Oswald", sans-serif; font-weight: 700;
    font-size: 22px; color: var(--text-grey); line-height: 26px; }
  .gig-text { position: absolute; font-size: 14.5px; line-height: 18px; color: var(--text-muted); }
  .more { position: absolute; font-size: 11px; color: var(--text-light); }
  .divider { position: absolute; left: 39px; top: 871px; width: 463px; height: 2px;
    background: linear-gradient(#555, #888); }

  .gig-circle { position: absolute; left: 638px; width: 74px; height: 74px; border-radius: 50%;
    background: var(--circle); font-family: "Oswald", sans-serif; font-weight: 700; font-size: 22px;
    line-height: 74px; text-align: center; color: var(--text-light); }

  .contact { position: absolute; right: 40px; top: 940px; text-align: right;
    font-family: "Oswald", sans-serif; font-weight: 300; white-space: nowrap; }
  .contact-phone { font-size: 38px; line-height: 48px; color: var(--text-light); }
  .contact-email { font-size: 34px; line-height: 44px; color: var(--accent-green); }

  /* Footer */
  .footer-rule { position: absolute; left: 0; top: 1051px; width: 1200px; height: 17px;
    background: linear-gradient(#222 0 30%, #6a6a6a 30% 55%, #111 55%); }
  .site-footer { position: absolute; left: 0; top: 1068px; width: 1200px; height: 117px; background: var(--bg-footer); }
  .footer-links { position: absolute; left: 24px; top: 25px; font-size: 13.5px; color: #d0d0d0; }
  .copyright { position: absolute; left: 24px; top: 49px; font-size: 12.5px; color: #888; }
  .social { position: absolute; top: 34px; display: flex; align-items: center; gap: 7px;
    font-family: "Oswald", sans-serif; font-weight: 400; font-size: 17px; color: var(--text-light); }
  .social i { display: block; width: 14px; height: 14px; background: var(--text-light); }
</style>
</head>
<body>

<header class="site-header">
  <a class="brand" href="#"><span class="brand-dot"></span>DJ-VORN</a>
  <nav class="main-nav">
    <a href="#" style="left:514px">HOME</a>
    <a href="#" style="left:606px">BOOKING</a>
    <a href="#" style="left:720px">RECENT GIGZ</a>
    <a href="#" style="left:856px">UPCOMING GIGZ</a>
    <a href="#" style="left:1014px">GALLERY</a>
    <a href="#" style="left:1124px">CONTACT</a>
  </nav>
</header>

<section class="hero" role="img" aria-label="Dark backdrop with sweeping orange, blue and green light streaks">
  <div class="hero-dj" role="img" aria-label="Photo of DJ-Vorn in headphones throwing a rock hand sign"></div>
  <div class="hero-decks" role="img" aria-label="Photo of a DJ controller with two turntables"></div>
  <p class="hero-text" style="left:83px; top:196px; width:300px;">
    Catch DJ Vorn at<br><span class="venue">Brixton's Loadhouse</span><br>on Corvell.
  </p>
  <p class="hero-text" style="left:790px; top:218px; width:400px;">
    Every Thursday for "<span class="night">Static Riot</span>"<br>and<br>Saturday for "<span class="night">Arcade Saturdays</span>".
  </p>
</section>

<div class="band"></div>

<a class="booking-btn" href="#"><span>REQUEST FOR BOOKING</span></a>

<h2 class="section-title recent-title">RECENT GIGZ</h2>

<article>
  <div class="gig-thumb" style="top:757px" role="img" aria-label="Photo of the DJ at a club night"></div>
  <div class="gig-date" style="top:755px">06.11.2013</div>
  <p class="gig-text" style="left:162px; top:777px; width:355px;">New mix up and running, ready for auditory pleasure making - just in time for your Australia Day festivities! Enjoy the beginning of a new trilogy ....</p>
  <a class="more" href="#" style="left:163px; top:840px">MORE</a>
</article>

<div class="divider"></div>

<article>
  <div class="gig-thumb alt" style="top:900px" role="img" aria-label="Photo of the DJ with a friend under green lights"></div>
  <div class="gig-date" style="top:898px">05.28.2013</div>
  <p class="gig-text" style="left:162px; top:920px; width:355px;">New mix up and running, ready for auditory pleasure making - just in time for your Australia Day festivities! Enjoy the beginning of a new trilogy of ....</p>
  <a class="more" href="#" style="left:161px; top:979px">MORE</a>
</article>

<h2 class="section-title upcoming-title">UPCOMING GIGZ</h2>

<article>
  <div class="gig-circle" style="top:666px">07.11</div>
  <p class="gig-text" style="left:736px; top:669px; width:432px;">New mix up and running, ready for auditory pleasure making - just in time for your Australia Day festivities! Enjoy the beginning of a new trilogy of mini-mixes I'll be releasing over the next few weeks. As always, love your feedback ....</p>
  <a class="more" href="#" style="left:736px; top:747px">MORE</a>
</article>

<article>
  <div class="gig-circle" style="top:799px">06.25</div>
  <p class="gig-text" style="left:736px; top:804px; width:432px;">New mix up and running, ready for auditory pleasure making - just in time for your Australia Day festivities! Enjoy the beginning of a new trilogy of mini-mixes I'll be releasing over the next few weeks. As always, love your feedback. ...</p>
  <a class="more" href="#" style="left:736px; top:889px">MORE</a>
</article>

<div class="contact">
  <p class="contact-phone">phone : 0491 570 118</p>
  <p class="contact-email">vornhq@mailbox.example</p>
</div>

<div class="footer-rule"></div>
<footer class="site-footer">
  <p class="footer-links">HOME | BOOKING | RECENT GIGZ | UPCOMING GIGZ | GALLERY | CONTACT</p>
  <p class="copyright">© Copyright DJ-VORN. All Rights Reserved 2013.</p>
  <a class="social" href="https://www.pagelinker.example/pages/DJ-Vorn/730162948415207" style="left:900px"><i></i>Pagelinker</a>
  <a class="social" href="#" style="left:1002px"><i></i>Tunedrift</a>
  <a class="social" href="#" style="left:1094px"><i></i>Chirpline</a>
</footer>

</body>
</html>
```